Create the ONLY Supplement line for Male Entrepreneurs! (Veltro Prime MD)

I need a label designed for a new supplement brand that I am launching.

There are five products so need a design that I can simply change the wording for each individual product

The brand name is called veltro prime MD. The focus is male entrepreneurial health.

Target audience is men 35 to 55.

Concepts: the healthier you are in body the more money you will make in business.

Concept to copy: I want to make a clean minimalistic label mimicking Dallamore MD (google it and you'll see what I mean)

Target Market(s)

male entrepreneurs 35-55

Industry/Entity Type

Health Supplement

Colors

Designer to choose colors to be used in the design.

Requirements
Must have
• Modern classy design, similar to Dallamore MD.
Nice to have
• Highlight that the supplement is Doctor Approved.
Should not have
• No loud colors. Present it as high class.

```html
<!DOCTYPE html>
<html lang="en">
<head>
<meta charset="utf-8">
<title>Veltro Prime MD — Vitamins for Men label</title>
<link rel="stylesheet" href="https://fonts.googleapis.com/css2?family=Montserrat:wght@300;400;600&display=swap">
<style>
  :root {
    --canvas-bg: #ffffff;
    --label-light: #e4e4e4;
    --label-mid: #cbcbcb;
    --label-dark: #bdbdbd;
    --ink-strong: #3a3a3a;
    --ink-soft: #4d4d4d;
    --rule: #3f3f3f;
  }
  html, body {
    margin: 0;
    padding: 0;
    width: 1200px;
    height: 1200px;
    overflow: hidden;
    background: var(--canvas-bg);
    font-family: "Montserrat", sans-serif;
  }
  .canvas {
    position: relative;
    width: 1200px;
    height: 1200px;
  }
  .label {
    position: absolute;
    left: 189px;
    top: 80px;
    width: 823px;
    height: 1040px;
    background: linear-gradient(90deg, var(--label-light) 0%, var(--label-mid) 45%, var(--label-dark) 70%, var(--label-light) 100%);
  }
  .brand-name {
    position: absolute;
    left: 420px;
    top: 130px;
    width: 290px;
    text-align: right;
    font-weight: 400;
    font-size: 44px;
    line-height: 1.1;
    color: var(--ink-strong);
  }
  .male-icon {
    position: absolute;
    left: 575px;
    top: 578px;
    width: 82px;
    height: 82px;
  }
  .product-name {
    position: absolute;
    left: 130px;
    top: 738px;
    margin: 0;
    font-weight: 600;
    font-size: 58px;
    letter-spacing: 3px;
    color: var(--ink-soft);
    white-space: nowrap;
  }
  .tagline {
    position: absolute;
    left: 135px;
    top: 838px;
    margin: 0;
    font-weight: 400;
    font-size: 27px;
    letter-spacing: 3px;
    color: var(--ink-soft);
    white-space: nowrap;
  }
  .divider {
    position: absolute;
    left: 135px;
    top: 898px;
    width: 558px;
    height: 10px;
    background: var(--rule);
  }
  .claim, .count {
    position: absolute;
    left: 135px;
    margin: 0;
    font-weight: 300;
    font-size: 32px;
    color: var(--ink-soft);
    white-space: nowrap;
  }
  .claim { top: 938px; }
  .count { top: 995px; }
</style>
</head>
<body>
<div class="canvas">
  <section class="label">
    <div class="brand-name">veltro prime MD</div>

    <svg class="male-icon" viewBox="0 0 82 82" aria-hidden="true">
      <circle cx="30" cy="52" r="22" fill="none" stroke="#3a3a3a" stroke-width="8"/>
      <line x1="46" y1="36" x2="74" y2="8" stroke="#3a3a3a" stroke-width="8"/>
      <polyline points="50,8 74,8 74,32" fill="none" stroke="#3a3a3a" stroke-width="8"/>
    </svg>

    <h1 class="product-name">VITAMINS FOR MEN</h1>
    <p class="tagline">MALE ENTREPRENEURIAL HEALTH</p>
    <div class="divider"></div>
    <p class="claim">Doctor Approved supplement</p>
    <p class="count">60 capsules</p>
  </section>
</div>
</body>
</html>
```